VKTO Meridian LLC Website

Basic website for a start up business in the defense and federal space. If we could have intelligence analysis and technology as a focus that would be great. Looking to use our core colors but a lighter set of web pages would be preferable

Target Market(s)

Defense

Coding

Coded - Design and coding required

Number of Pages Required

3 page

```html
<!DOCTYPE html>
<html lang="en">
<head>
<meta charset="utf-8">
<title>VKTO Meridian LLC — Intelligence Analysis and Technology</title>
<link rel="stylesheet" href="https://fonts.googleapis.com/css2?family=Syncopate:wght@400;700&family=Roboto:wght@400;500;700&display=swap">
<style>
:root{
  --red:#c6093b;
  --red-deep:#8e0a2c;
  --ink:#1c1c22;
  --dark:#17161b;
  --grey:#e7e7e9;
  --text:#4a4a52;
  --line:#cfcfd4;
  --white:#ffffff;
  --head:"Syncopate", "Arial Black", sans-serif;
  --body:"Roboto", Arial, sans-serif;
}
*{box-sizing:border-box;margin:0;padding:0}
html,body{width:1200px;height:4494px;overflow:hidden;background:var(--white)}
body{font-family:var(--body);color:var(--text)}
.page{position:relative;width:1200px;height:4494px;overflow:hidden}
.abs{position:absolute}
a{color:inherit;text-decoration:none}

/* header */
.site-header{position:absolute;left:0;top:0;width:1200px;height:78px;background:var(--white)}
.brand{position:absolute;left:119px;top:26px;font-family:var(--head);font-weight:700;font-size:20px;color:var(--ink);letter-spacing:1px;display:flex;align-items:center;gap:10px}
.brand-dot{width:12px;height:12px;background:var(--red);border-radius:50%}
.main-nav a{position:absolute;top:34px;font-size:13px;color:#555;letter-spacing:.3px}
.main-nav a.active{color:var(--ink);font-weight:500}
.main-nav a.active::after{content:"";position:absolute;left:0;right:0;top:20px;height:2px;background:var(--red);border-radius:2px}
.btn-solid{position:absolute;display:flex;align-items:center;justify-content:center;background:var(--red);color:var(--white);border-radius:24px;font-weight:700;font-size:13px;letter-spacing:.3px}
.btn-outline{position:absolute;display:flex;align-items:center;justify-content:center;border:2px solid var(--red);color:var(--red);border-radius:24px;font-weight:700;font-size:12px;letter-spacing:.3px;background:transparent}

/* hero */
.hero{position:absolute;left:0;top:78px;width:1200px;height:609px}
.hero-photo{position:absolute;inset:0;background:linear-gradient(90deg,#000 0%,#060a14 20%,#13233b 45%,#0d3a6e 70%,#0a4d8c 100%)}
.hero-title{position:absolute;left:117px;top:182px;font-family:var(--head);font-size:33px;line-height:39px;color:var(--white);font-weight:400}
.hero-title b{font-weight:700}
.hero-title .accent{color:var(--red)}
.hero-text{position:absolute;left:119px;top:314px;width:370px;font-size:14px;line-height:20px;color:#d9dbe2}
.hero-arrow{position:absolute;top:258px}

/* section headings */
.sec-title{position:absolute;font-family:var(--head);font-size:30px;line-height:34px;color:var(--ink);font-weight:400}
.sec-title b{font-weight:700}
.sec-title .red{color:var(--red)}
.sec-rule{position:absolute;width:46px;height:3px;background:var(--red)}
.copy{position:absolute;font-size:14.5px;line-height:24px;color:var(--text)}

/* about */
.about{position:absolute;left:0;top:687px;width:1200px;height:625px;background:linear-gradient(180deg,#fafafb,#f1f1f4)}
.feature-cards{position:absolute;left:138px;top:342px;width:931px;height:209px;display:flex;border:1px solid var(--line);background:var(--white)}
.feature-card{flex:1;display:flex;flex-direction:column;align-items:center;padding-top:26px;text-align:center}
.feature-card h3{font-family:var(--head);font-weight:700;font-size:14px;color:var(--ink);margin:14px 0 12px;letter-spacing:.5px}
.feature-card p{font-size:11.5px;line-height:18px;color:var(--text);width:240px}
.feature-card.is-active{background:linear-gradient(90deg,var(--red-deep),#3a0714 110%)}
.feature-card.is-active h3,.feature-card.is-active p{color:var(--white)}

/* intelligence */
.intel{position:absolute;left:0;top:1312px;width:1200px;height:540px;background:var(--grey);overflow:hidden}
.photo-circle{position:absolute;border-radius:50%}

/* technology */
.tech{position:absolute;left:0;top:1852px;width:1200px;height:598px;background:radial-gradient(ellipse at 50% 80%,#2a2a31,var(--dark) 70%);overflow:hidden}
.tech-title{position:absolute;left:0;width:1200px;top:96px;text-align:center;font-family:var(--head);font-size:28px;color:var(--white);font-weight:400}
.tech-title b{font-weight:700}
.tech-copy{position:absolute;left:230px;width:740px;top:146px;text-align:center;font-size:14.5px;line-height:24.5px;color:#d2d2d8}
.tech-item{position:absolute;top:284px;width:300px;display:flex;gap:14px;align-items:flex-start}
.tech-icon{width:74px;height:74px;border-radius:50%;flex:none;display:flex;align-items:center;justify-content:center}
.tech-item h4{font-size:13.5px;font-weight:700;color:var(--white);margin:10px 0 6px;letter-spacing:.3px}
.tech-item p{font-size:11.5px;line-height:17px;color:#c9c9cf}

/* projects */
.projects{position:absolute;left:0;top:2450px;width:1200px;height:579px;background:var(--white)}
.project{position:absolute;width:298px;height:208px;border-radius:4px;overflow:hidden}
.project span{position:absolute;left:25px;bottom:18px;font-size:16px;font-weight:500;color:var(--white);letter-spacing:.4px}

/* why */
.why{position:absolute;left:0;top:3029px;width:1200px;height:543px;background:var(--grey);overflow:hidden}

/* contact */
.contact{position:absolute;left:0;top:3572px;width:1200px;height:558px;background:linear-gradient(180deg,#fff,#f4f4f6)}
.eyebrow{position:absolute;left:148px;top:114px;font-size:14px;color:#777;letter-spacing:.4px}
.contact-title{position:absolute;left:146px;top:144px;font-family:var(--head);font-size:29px;line-height:34px;color:var(--red);font-weight:400}
.contact-title b{display:block;color:var(--ink);font-weight:700}
.contact-icon{position:absolute;width:64px;height:64px;border-radius:50%;border:1px solid var(--line);background:var(--white);display:flex;align-items:center;justify-content:center}
.contact-label{position:absolute;font-size:13px;color:#444}
.contact-value{position:absolute;font-size:15.5px;color:var(--ink)}
.form-card{position:absolute;left:586px;top:82px;width:483px;height:375px;background:var(--white);box-shadow:0 6px 30px rgba(0,0,0,.08)}
.field{position:absolute;left:45px;width:396px;height:42px;border:1px solid #b9b9c0;display:flex;align-items:center;gap:10px;padding-left:14px;font-size:12.5px;color:#555}
.field.message{height:80px;align-items:flex-start;padding-top:12px;padding-left:18px}

/* footer */
.site-footer{position:absolute;left:0;top:4130px;width:1200px;height:300px;background:var(--ink)}
.footer-brand{position:absolute;left:112px;top:76px;font-family:var(--head);font-weight:700;font-size:22px;color:var(--white);letter-spacing:1px}
.social{position:absolute;top:166px;width:28px;height:28px;border-radius:50%;background:var(--white)}
.footer-div{position:absolute;top:74px;width:3px;height:26px;background:var(--white)}
.footer-col h5{position:absolute;top:76px;font-size:13.5px;font-weight:700;color:var(--white);letter-spacing:.4px}
.footer-link{position:absolute;font-size:11.5px;color:#bdbdc4}
.copyright{position:absolute;left:0;top:4430px;width:1200px;height:64px;background:#0b0b0d;color:#aaa;font-size:11px;display:flex;align-items:center;justify-content:center}
</style>
</head>
<body>
<div class="page">

  <header class="site-header">
    <div class="brand"><span class="brand-dot"></span>VKTO MERIDIAN</div>
    <nav class="main-nav">
      <a class="active" style="left:358px">ABOUT</a>
      <a style="left:466px">SERVICES</a>
      <a style="left:591px">TECHNOLOGY</a>
      <a style="left:740px">ANALYTICS</a>
      <a style="left:872px">BLOGS</a>
    </nav>
    <a class="btn-solid" style="left:956px;top:23px;width:129px;height:38px">CONTACT US</a>
  </header>

  <section class="hero">
    <div class="hero-photo" role="img" aria-label="Two analysts studying a wall of glowing blue data screens in a dark operations room"></div>
    <h1 class="hero-title"><b>INTELLIGENCE</b><br>ANALYSIS AND<br><span class="accent">TECHNOLOGY</span></h1>
    <p class="hero-text">Lorem ipsum dolor sit amet, consectetur adipiscing elit, sed do eiusmod tempor incididunt ut labore.</p>
    <a class="btn-solid" style="left:119px;top:375px;width:165px;height:46px">EXPLORE MORE</a>
    <svg class="hero-arrow" style="left:32px" width="22" height="40" viewBox="0 0 22 40"><path d="M17 4 L5 20 L17 36" fill="none" stroke="#fff" stroke-width="4"/></svg>
    <svg class="hero-arrow" style="left:1142px" width="22" height="40" viewBox="0 0 22 40"><path d="M5 4 L17 20 L5 36" fill="none" stroke="#fff" stroke-width="4"/></svg>
  </section>

  <section class="about">
    <svg class="abs" style="left:0;top:0" width="1200" height="625" viewBox="0 0 1200 625">
      <path d="M0 332 C160 300 290 250 384 187 L355 187 C280 240 150 290 0 314 Z" fill="var(--red)"/>
      <path d="M222 187 H384 L372 197 H225 Z" fill="var(--red)"/>
    </svg>
    <h2 class="sec-title" style="left:127px;top:90px"><span class="red">ABOUT</span><br>VKTO <b>MERIDIAN</b></h2>
    <p class="copy" style="left:515px;top:95px;width:545px;font-size:15.5px;line-height:27px">Lorem ipsum dolor sit amet, consectetur adipiscing elit, sed do eiusmod tempor incididunt ut labore et dolore magna aliqua. Ut enim ad minim veniam, quis nostrud exercitation ullamco la</p>

    <div class="feature-cards">
      <div class="feature-card">
        <svg width="48" height="48" viewBox="0 0 48 48" fill="none" stroke="var(--red)" stroke-width="2"><circle cx="24" cy="22" r="15"/><path d="M24 7v30M13 14h22M11 24h26M15 32h18"/><circle cx="24" cy="22" r="4" fill="var(--red)"/><path d="M18 40h12"/></svg>
        <h3>INTELLIGENCE</h3>
        <p>Lorem ipsum dolor sit amet, consectetur adipiscing sum dolor sit.Lorem ipsum dolor sit amet, consectetur adipiscing</p>
      </div>
      <div class="feature-card is-active">
        <svg width="56" height="48" viewBox="0 0 56 48" fill="none" stroke="#fff" stroke-width="2"><rect x="4" y="14" width="34" height="26"/><path d="M10 34V26M17 34V22M24 34V28M31 34V20"/><circle cx="44" cy="14" r="9"/><path d="M50 20l5 5"/><path d="M6 10h10M6 6h16"/></svg>
        <h3>ANALYSIS</h3>
        <p>Lorem ipsum dolor sit amet, consectetur adipiscing sum dolor sit.Lorem ipsum dolor sit amet, consectetur adipiscing</p>
      </div>
      <div class="feature-card">
        <svg width="48" height="48" viewBox="0 0 48 48" fill="none" stroke="var(--red)" stroke-width="2"><rect x="8" y="12" width="32" height="22"/><path d="M16 40h16M24 34v6M14 6h4v6M22 4h4v8M30 6h4v6"/><circle cx="24" cy="23" r="5"/></svg>
        <h3>TECHNOLOGY</h3>
        <p>Lorem ipsum dolor sit amet, consectetur adipiscing sum dolor sit.Lorem ipsum dolor sit amet, consectetur adipiscing</p>
      </div>
    </div>
  </section>

  <section class="intel">
    <svg class="abs" style="left:0;top:0" width="1200" height="540" viewBox="0 0 1200 540">
      <path d="M755 0 H1200 V540 H742 C736 480 770 440 850 420 C1010 380 1080 250 1030 140 C990 60 880 25 755 0 Z" fill="var(--red)"/>
      <circle cx="823" cy="266" r="227" fill="none" stroke="#bdbdc4" stroke-width="1.5"/>
      <circle cx="823" cy="266" r="210" fill="none" stroke="#fff" stroke-width="1" opacity=".7"/>
      <circle cx="942" cy="91" r="6" fill="#fff"/>
      <circle cx="664" cy="401" r="6" fill="var(--ink)"/>
    </svg>
    <div class="photo-circle" role="img" aria-label="Hand touching a holographic dashboard of charts and data panels" style="left:635px;top:78px;width:376px;height:376px;background:radial-gradient(circle at 40% 40%,#3b7fd0,#15407e 60%,#0b2550)"></div>
    <h2 class="sec-title" style="left:131px;top:104px">INTELLIGENCE<br><b class="red">ANALYSIS</b></h2>
    <div class="sec-rule" style="left:131px;top:174px"></div>
    <p class="copy" style="left:129px;top:197px;width:440px">Lorem ipsum dolor sit amet, consectetur adipiscing elit, sed do eiusmod tempor incididunt ut</p>
    <p class="copy" style="left:129px;top:265px;width:440px">Ut enim ad minim veniam, quis nostrud exercitation ullamco laboris nisi ut aliquip ex ea commodo consequat. Duis aute irure dolor in reprehenderit in voluptate velit esse cillum dolore eu fugiat nulla s nostrud exercitation ullamco laboris</p>
    <a class="btn-outline" style="left:126px;top:385px;width:158px;height:42px">LEARN MORE</a>
  </section>

  <section class="tech">
    <svg class="abs" style="left:0;top:0" width="1200" height="598" viewBox="0 0 1200 598">
      <path d="M0 520 L340 390 L340 410 L0 545 Z" fill="var(--red)"/>
      <path d="M0 545 C300 600 700 640 1200 430 V598 H0 Z" fill="var(--red)"/>
      <path d="M0 560 C320 615 720 640 1200 455 V598 H0 Z" fill="#fff"/>
    </svg>
    <h2 class="tech-title">OUR <b>TECHNOLOGY</b></h2>
    <div class="sec-rule" style="left:577px;top:136px"></div>
    <p class="tech-copy">Lorem ipsum dolor sit amet, consectetur adipiscing elit, sed do eiusmod tempor incididunt ut Ut enim ad minim veniam, quis nostrud exercitation ullamco laboris nisi ut aliquip ex ea commodo consequat. Duis aute irure dolor in reprehenderit in voluptate velit esse cillum dolore.</p>

    <div class="tech-item" style="left:124px">
      <div class="tech-icon" style="background:var(--red)"><svg width="36" height="32" viewBox="0 0 36 32" fill="none" stroke="#fff" stroke-width="2"><rect x="3" y="3" width="30" height="20"/><path d="M12 29h12M18 23v6M9 17l6-6 5 4 7-7"/></svg></div>
      <div><h4>LOREM IPSUM DOLOR</h4><p>Consectetur adipiscing elit sed do eius-mod tempor incididunt ut.</p></div>
    </div>
    <div class="tech-item" style="left:452px">
      <div class="tech-icon" style="background:#d8d8dc"><svg width="30" height="36" viewBox="0 0 30 36" fill="none" stroke="#555" stroke-width="2"><path d="M15 3a10 10 0 0 0-6 18v5h12v-5a10 10 0 0 0-6-18z"/><path d="M10 30h10M12 34h6"/></svg></div>
      <div><h4>LOREM IPSUM DOLOR</h4><p>Consectetur adipiscing elit sed do eius-mod tempor incididunt ut.</p></div>
    </div>
    <div class="tech-item" style="left:778px">
      <div class="tech-icon" style="background:#3a3a42"><svg width="34" height="34" viewBox="0 0 34 34" fill="none" stroke="#ddd" stroke-width="2"><circle cx="17" cy="17" r="13"/><circle cx="17" cy="17" r="6"/><path d="M17 2v6M17 26v6M2 17h6M26 17h6"/></svg></div>
      <div><h4>LOREM IPSUM DOLOR</h4><p>Consectetur adipiscing elit sed do eius-mod tempor incididunt ut.</p></div>
    </div>
  </section>

  <section class="projects">
    <h2 class="sec-title" style="left:120px;top:175px">OUR LATEST<br><b class="red">PROJECTS</b></h2>
    <div class="sec-rule" style="left:120px;top:245px"></div>
    <p class="copy" style="left:119px;top:278px;width:300px">Lorem ipsum dolor sit amet, consectetur adipiscing elit, sed do eiusmod tempor incididunt ut Ut enim ad minim veniam, quis nostrud exercitation</p>
    <a class="btn-outline" style="left:119px;top:398px;width:158px;height:42px">LEARN MORE</a>

    <div class="project" style="left:483px;top:75px;background:linear-gradient(160deg,#d9d9dc,#6e6e76 60%,#2a2c38)" role="img" aria-label="Hand writing with a pen over financial charts"><span>SEDUT PERSPICIATIS UNDE</span></div>
    <div class="project" style="left:485px;top:302px;background:linear-gradient(160deg,#c9cbd0,#5d6670 55%,#1f2530)" role="img" aria-label="Hands typing on a keyboard beside market charts"><span>UT ENIM AD MINIMA</span></div>
    <div class="project" style="left:799px;top:197px;background:linear-gradient(150deg,#0b1f4a,#1b4fa0 55%,#0b2250)" role="img" aria-label="Person pointing at a glowing blue holographic chart"><span>NEQUE PORRO QUISQUAM</span></div>
  </section>

  <section class="why">
    <svg class="abs" style="left:0;top:0" width="1200" height="543" viewBox="0 0 1200 543">
      <path d="M0 0 H440 C270 50 150 170 170 300 C190 420 390 450 445 543 H0 Z" fill="var(--red)"/>
      <circle cx="366" cy="258" r="227" fill="none" stroke="#fff" stroke-width="1.2" opacity=".8"/>
      <circle cx="245" cy="88" r="6" fill="#fff"/>
      <circle cx="523" cy="402" r="6" fill="var(--ink)"/>
    </svg>
    <div class="photo-circle" role="img" aria-label="Team of colleagues reviewing plans together at a desk" style="left:178px;top:70px;width:376px;height:376px;background:radial-gradient(circle at 45% 40%,#b9c7d8,#5d7da6 55%,#28466f)"></div>
    <h2 class="sec-title" style="left:635px;top:115px">WHY CHOOSE<br><b class="red">VKTO MERIDIAN</b></h2>
    <div class="sec-rule" style="left:635px;top:185px"></div>
    <p class="copy" style="left:633px;top:207px;width:440px">Lorem ipsum dolor sit amet, consectetur adipiscing elit, sed do eiusmod tempor incididunt ut</p>
    <p class="copy" style="left:633px;top:275px;width:440px">Ut enim ad minim veniam, quis nostrud exercitation ullamco laboris nisi ut aliquip ex ea commodo consequat. Duis aute irure dolor in reprehenderit in voluptate velit esse cillum dolore eu fugiat nulla s nostrud exercitation ullamco laboris</p>
    <a class="btn-outline" style="left:631px;top:398px;width:158px;height:44px">LEARN MORE</a>
  </section>

  <section class="contact">
    <p class="eyebrow">GET IN TOUCH</p>
    <h2 class="contact-title">CONTACT VKTO<b>MERIDIAN LLC</b></h2>

    <div class="contact-icon" style="left:141px;top:254px"><svg width="28" height="28" viewBox="0 0 28 28" fill="none" stroke="var(--red)" stroke-width="1.8"><path d="M6 3l5 1 2 6-3 2c1.5 3 3.5 5 6.5 6.5l2-3 6 2 1 5c-1 1.5-3 2.5-5 2C11 24 4 17 3 8c-.5-2 .5-4 3-5z"/></svg></div>
    <span class="contact-label" style="left:219px;top:262px">Phone Number</span>
    <span class="contact-value" style="left:219px;top:284px">(+958) 5550 2187</span>

    <div class="contact-icon" style="left:141px;top:334px"><svg width="28" height="22" viewBox="0 0 28 22" fill="none" stroke="var(--red)" stroke-width="1.8"><rect x="2" y="2" width="24" height="18"/><path d="M2 3l12 9 12-9"/></svg></div>
    <span class="contact-label" style="left:219px;top:344px">Email address</span>
    <span class="contact-value" style="left:219px;top:366px">info@vktomeridian.com</span>

    <form class="form-card">
      <div class="field" style="top:47px"><svg width="14" height="14" viewBox="0 0 14 14" fill="none" stroke="#888" stroke-width="1.2"><circle cx="7" cy="4.5" r="3"/><path d="M1.5 13c.5-3 2.7-4.5 5.5-4.5s5 1.5 5.5 4.5"/></svg>Name</div>
      <div class="field" style="top:101px"><svg width="14" height="12" viewBox="0 0 14 12" fill="none" stroke="#888" stroke-width="1.2"><rect x="1" y="1" width="12" height="10"/><path d="M1 2l6 5 6-5"/></svg>Email address</div>
      <div class="field" style="top:153px"><svg width="14" height="14" viewBox="0 0 28 28" fill="none" stroke="#888" stroke-width="2.2"><path d="M6 3l5 1 2 6-3 2c1.5 3 3.5 5 6.5 6.5l2-3 6 2 1 5c-1 1.5-3 2.5-5 2C11 24 4 17 3 8c-.5-2 .5-4 3-5z"/></svg>Phone Number</div>
      <div class="field message" style="top:204px">Message</div>
      <a class="btn-solid" style="left:45px;top:305px;width:152px;height:40px;font-size:12.5px">SUBMIT NOW</a>
    </form>
  </section>

  <footer class="site-footer">
    <div class="footer-brand">VKTO MERIDIAN</div>
    <span class="social" style="left:183px"></span>
    <span class="social" style="left:218px"></span>
    <span class="social" style="left:252px"></span>
    <span class="social" style="left:286px"></span>

    <span class="footer-div" style="left:407px"></span>
    <span class="footer-div" style="left:639px"></span>
    <span class="footer-div" style="left:862px"></span>

    <div class="footer-col">
      <h5 style="left:453px">NAVIGATION</h5>
      <a class="footer-link" style="left:453px;top:111px">About Us</a>
      <a class="footer-link" style="left:453px;top:139px">Our Services</a>
      <a class="footer-link" style="left:453px;top:167px">Why We Are</a>
      <a class="footer-link" style="left:453px;top:196px">Projects</a>
    </div>
    <div class="footer-col">
      <h5 style="left:689px">RESOURCES</h5>
      <a class="footer-link" style="left:689px;top:111px">Terms &amp; Condition</a>
      <a class="footer-link" style="left:689px;top:139px">Privacy Policy</a>
      <a class="footer-link" style="left:689px;top:167px">Blogs</a>
      <a class="footer-link" style="left:689px;top:196px">Contact Us</a>
    </div>
    <div class="footer-col">
      <h5 style="left:900px">CONTACT US</h5>
      <svg class="abs" style="left:897px;top:117px" width="26" height="26" viewBox="0 0 28 28" fill="none" stroke="var(--red)" stroke-width="1.8"><path d="M6 3l5 1 2 6-3 2c1.5 3 3.5 5 6.5 6.5l2-3 6 2 1 5c-1 1.5-3 2.5-5 2C11 24 4 17 3 8c-.5-2 .5-4 3-5z"/></svg>
      <span class="footer-link" style="left:934px;top:113px;font-size:10px;color:#999">Phone Number</span>
      <span class="footer-link" style="left:934px;top:130px;color:#fff">(+958) 5550 2187</span>
      <svg class="abs" style="left:897px;top:174px" width="28" height="22" viewBox="0 0 28 22" fill="none" stroke="var(--red)" stroke-width="1.8"><rect x="2" y="2" width="24" height="18"/><path d="M2 3l12 9 12-9"/></svg>
      <span class="footer-link" style="left:934px;top:166px;font-size:10px;color:#999">Email address</span>
      <span class="footer-link" style="left:934px;top:183px;color:#fff">info@vktomeridian.com</span>
    </div>
  </footer>
  <div class="copyright">© 2022 VKTO Meridian &nbsp;| All Rights Reserved</div>

</div>
</body>
</html>
```